Business Card Design

Im looking for a business card that will market/promote myself as in independent/freelancer in the beauty industry. Im looking for something very modern, and clean looking. no specific colors just something that doesnt look cheesy, would like a very professional look

Industry/Entity Type

Business

Contact Information for Business Card

Corinne Baldasso, Hairstylist(Cut, color, blowdry, style, extensions, straightening treatments), makeup artist, red carpet, in-salon, editorial, tv, film, contact is 5073914620 cbstyling@quillmail.net, LA based

```html
<!DOCTYPE html>
<html lang="en">
<head>
<meta charset="utf-8">
<title>Corinne Baldasso — Business Card</title>
<link rel="stylesheet" href="https://fonts.googleapis.com/css2?family=Carlito&display=swap">
<style>
  :root {
    --paper: #ffffff;
    --card: #070a09;
    --ink: #d5dfe0;
    --rule: #e4e8e8;
  }
  html, body {
    margin: 0;
    padding: 0;
    width: 1200px;
    height: 702px;
    overflow: hidden;
    background: var(--paper);
  }
  .business-card {
    position: absolute;
    left: 13px;
    top: 11px;
    width: 1174px;
    height: 679px;
    background: var(--card);
  }
  .business-card svg {
    display: block;
    width: 100%;
    height: 100%;
  }
  .name-first,
  .name-last {
    font-family: "Carlito", "Calibri", sans-serif;
    fill: var(--ink);
  }
  .name-first { font-size: 148px; letter-spacing: 1px; }
  .name-last  { font-size: 120px; }
  .divider-rule { stroke: var(--rule); stroke-width: 1.6; }
</style>
</head>
<body>
  <main class="business-card">
    <svg viewBox="0 0 1174 679" xmlns="http://www.w3.org/2000/svg" aria-label="Corinne Baldasso">
      <text class="name-first" x="575" y="453" text-anchor="middle">corinne</text>
      <line class="divider-rule" x1="48" y1="453" x2="1127" y2="453"/>
      <text class="name-last" x="578" y="535" text-anchor="middle">Baldasso</text>
    </svg>
  </main>
</body>
</html>
```